Torvane Systems*

Stationary design including business cards, letter heads, envelops and email signatures using our new logo

Target Market(s)

Innovative Technologies

Industry/Entity Type

Defense Contracting

Font styles to use
Sans Serif

```html
<!DOCTYPE html>
<html lang="en">
<head>
<meta charset="utf-8">
<title>Torvane Systems Letterhead</title>
<link rel="stylesheet" href="https://fonts.googleapis.com/css2?family=Montserrat:wght@300;400;500&display=swap">
<style>
  :root {
    --backdrop: #d9dadc;
    --paper: #ffffff;
    --ink: #1f1c1d;
    --band: #231f20;
    --band-text: #ffffff;
    --signature: #1b2fd6;
    --signature-fill: #dfe3fb;
  }
  * { margin: 0; padding: 0; box-sizing: border-box; }
  html, body {
    width: 1200px; height: 1200px; overflow: hidden;
    background: var(--backdrop);
    font-family: "Montserrat", sans-serif;
    color: var(--ink);
  }
  .letterhead {
    position: absolute; left: 237px; top: 85px;
    width: 727px; height: 1029px;
    background: var(--paper);
  }
  .brand {
    position: absolute; top: 190px; left: 0; width: 100%;
    text-align: center;
    font-family: "Montserrat", sans-serif;
    font-weight: 400; font-size: 22px; letter-spacing: 1px;
    color: var(--ink);
  }
  .letter-body {
    position: absolute; left: 104px; top: 346px; width: 520px;
    font-size: 13px; font-weight: 400; line-height: 16.2px;
    text-align: justify;
  }
  .letter-body p + p { margin-top: 16.2px; }
  .signature {
    position: absolute; left: 96px; top: 760px;
    width: 185px; height: 42px;
    background: var(--signature-fill);
  }
  .signer-role {
    position: absolute; left: 104px; top: 802px;
    font-size: 15px; font-weight: 400;
  }
  .contact-band {
    position: absolute; left: 0; bottom: 0; width: 100%; height: 79px;
    background: var(--band); color: var(--band-text);
    font-size: 11.5px; font-weight: 400;
    text-align: center;
  }
  .contact-line {
    position: absolute; top: 18px; left: 0; width: 100%;
    display: flex; justify-content: center; gap: 8px;
  }
  .contact-item { display: inline-flex; align-items: center; gap: 3px; }
  .contact-item svg { width: 11px; height: 11px; }
  .address-line { position: absolute; top: 43px; left: 0; width: 100%; }
</style>
</head>
<body>
  <main class="letterhead">
    <div class="brand">TORVANE SYSTEMS</div>

    <section class="letter-body">
      <p>Letterhead samples are a great way of deciding what kind of letterhead you want to design for you and your company. The internet has a ton of great letterhead samples to browse through. Whether you want something simple, with just a couple lines of text of your business information, or something decorative and stunning, with photos and logos on the top and bottom of the page, it will be easy to find what you want, because there are samples online for basically any type of letterhead you could want.</p>
      <p>Any business could easily benefit from browsing through some letterhead samples, if only to get an idea for what kind of letterhead their company might want. Letterheads are just one of the tools that a business professional could use to help increase their customer base, and to really be memorable to everyone they write a letter to. Letterhead is quite an effective tool for marketing and advertising, but because it’s such a simple and well known idea, it is often unfairly overlooked. Make sure you don’t make that mistake, and make some letterhead samples of your own today.</p>
      <p>Whether you want to get new customers to remember you and become part of your clientele, or you just want to send out friendly reminders to your existing clients, customizing your own letterhead samples can really help you out. Try out some letterhead samples and you will not regret it, and I’m sure you will add a new tool to your business’ arsenal of networking, marketing, and advertising tools.</p>
    </section>

    <div class="signature" role="img" aria-label="Handwritten signature of Elias Marrow in blue ink"></div>
    <div class="signer-role">company director</div>

    <footer class="contact-band">
      <div class="contact-line">
        <span class="contact-item">
          <svg viewBox="0 0 12 12" aria-hidden="true"><circle cx="6" cy="6" r="6" fill="#fff"/><path d="M4 3.2l1 1.4-.6.7c.4.9 1.1 1.6 2 2l.7-.6 1.4 1-.5 1.1C5.8 8.6 3.4 6.2 3.2 3.9z" fill="#231f20"/></svg>
          555 5555 5555
        </span>
        <span class="contact-item">
          <svg viewBox="0 0 12 12" aria-hidden="true"><circle cx="6" cy="6" r="6" fill="#fff"/><rect x="3" y="4" width="6" height="4.2" fill="#231f20"/><path d="M3 4l3 2.3L9 4" stroke="#fff" stroke-width=".7" fill="none"/></svg>
          e.marrow@torvanesystems.com
        </span>
        <span class="contact-item">
          <svg viewBox="0 0 12 12" aria-hidden="true"><circle cx="6" cy="6" r="6" fill="#fff"/><circle cx="6" cy="6" r="3.3" fill="none" stroke="#231f20" stroke-width=".8"/><path d="M2.7 6h6.6M6 2.7c-1.6 2-1.6 4.6 0 6.6M6 2.7c1.6 2 1.6 4.6 0 6.6" stroke="#231f20" stroke-width=".7" fill="none"/></svg>
          www.torvanesystems.com
        </span>
      </div>
      <div class="address-line">123 Fake Street, Anytown, New York 12345</div>
    </footer>
  </main>
</body>
</html>
```